Higher $ Now Guaranteed! Redesign Web Page(s) Style Composition and Color (Graphics design-not code)

We need a modern look for an existing website. You can either use or change the current logo. Choice of colors, fonts, style is up to you. Sample URLs and additional details are provided in the attached document. Most of our struggle has been the appearance of the directory listings (city) page.
----------------------------------------------------------------------------------
--> Increased Project Budget and Now Funds are GUARANTEED
--> Added an additional attachment in response to questions
-->THIS PROJECT IS FOR GRAPHICS/DESIGN NOT CODE
The project is mostly a few areas of text and colored boxes or lines. Hopefully a skilled designer can place these elements in an attractive layout and choose the right colors and styles. There are no complex drawings required for this project.

*** We are involved with other projects from time to time and expect that the winning designer will be given the first opportunity at this future work. ***

*** There is no requirement to do any code but if you submit a design feel free to indicate if you wish to be considered for any future code work on this site or others ***

Font styles to use
Sans Serif

Requirements
Must have
• Rounded corners on images and buttons with nice gradients or hover effects.
Nice to have
• Attached an additional descriptions document to help with these answers.
Should not have
• Small fonts, traditional older looking rectangular buttons, dull or boring color schemes

```html
<!DOCTYPE html>
<html lang="en">
<head>
<meta charset="utf-8">
<title>Directory of Bellevue Tax Experts</title>
<link href="https://fonts.googleapis.com/css2?family=Roboto:ital,wght@0,400;0,500;0,700;1,400&display=swap" rel="stylesheet">
<style>
:root{
  --blue:#1a8fd6;
  --blue-light:#2ea8ea;
  --green:#5cba1c;
  --green-light:#6fcc26;
  --orange:#f7931e;
  --orange-light:#ffa92f;
  --dark:#2b2b2b;
  --text:#3a3a3a;
  --line:#d6d6d6;
  --footer:#3a3a3a;
  --gold-top:#bf9a4b;
  --gold-bot:#e2b966;
  --amber-top:#c98a32;
  --amber-bot:#f3a843;
}
*{box-sizing:border-box;margin:0;padding:0}
html,body{width:900px;height:1200px;overflow:hidden}
body{font-family:'Roboto',sans-serif;color:var(--text);background:#fff;position:relative}
.abs{position:absolute}

/* header */
.site-header{position:absolute;left:0;top:0;width:900px;height:75px;background:linear-gradient(#fff,#f1f1f1);border-bottom:1px solid #d8d8d8}
.brand{position:absolute;left:56px;top:24px;display:flex;align-items:center;gap:6px;font-size:17px;font-weight:500;color:var(--dark)}
.brand-dot{width:14px;height:14px;border-radius:50%;background:var(--dark)}
.main-nav{position:absolute;left:399px;top:32px;display:flex;gap:29px;font-size:9.5px;color:var(--dark)}
.phone-pill{position:absolute;left:688px;top:22px;width:157px;height:28px;border-radius:5px;background:linear-gradient(var(--orange-light),var(--orange));color:#fff;font-weight:700;font-size:15px;line-height:28px;padding-left:40px}
.phone-icon{position:absolute;left:-1px;top:-2px;width:32px;height:32px;border-radius:50%;background:#3a3a3a;border:3px solid #e6e6e6;display:flex;align-items:center;justify-content:center}

/* hero */
.hero-band{position:absolute;left:0;top:76px;width:900px;height:425px;background:linear-gradient(#fff 60%,#efefef)}
.page-title{position:absolute;left:55px;top:96px;font-size:25px;line-height:30px;font-weight:500;color:var(--blue)}
.cta{position:absolute;left:528px;width:317px;height:54px;border-radius:3px;color:#fff;font-weight:700;font-size:14px;padding-left:14px;line-height:54px;box-shadow:0 6px 6px -4px rgba(0,0,0,.25)}
.cta.preparer{top:101px;background:linear-gradient(var(--blue-light),var(--blue))}
.cta.help{top:174px;background:linear-gradient(var(--green-light),var(--green))}
.cta-btn{position:absolute;right:14px;top:13px;height:28px;padding:0 14px;border-radius:4px;background:linear-gradient(#3a3a3a,#1e1e1e);font-size:9px;font-weight:500;line-height:28px;color:#fff}
.city-search{position:absolute;left:56px;top:171px;width:452px;height:58px;border:1px solid #d4d4d4;border-radius:3px;background:#f3f3f3}
.city-search label{position:absolute;left:9px;top:22px;font-size:10.5px;color:var(--dark)}
.city-select{position:absolute;left:70px;top:14px;width:274px;height:30px;border:1px solid #d6d6d6;border-radius:3px;background:#fff;font-size:10.5px;color:#777;padding-left:10px;line-height:28px}
.city-select::after{content:"";position:absolute;right:11px;top:12px;border:4px solid transparent;border-top:5px solid #aaa}
.go-btn{position:absolute;left:354px;top:14px;width:88px;height:30px;border-radius:3px;background:linear-gradient(var(--orange-light),var(--orange));color:#fff;font-size:10px;font-weight:500;text-align:center;line-height:30px;border:1px solid #e28610}
.rule{position:absolute;left:56px;top:256px;width:789px;height:1px;background:#d0d0d0}

/* featured */
.featured{position:absolute;top:280px;width:180px;height:192px;border-radius:3px;padding:18px 13px 0;font-size:9.5px;line-height:15px;box-shadow:0 8px 8px -6px rgba(0,0,0,.25)}
.featured h3{font-size:11px;line-height:14px;font-weight:500;color:#fff;padding-bottom:9px;border-bottom:1px solid rgba(255,255,255,.7);margin-bottom:12px}
.featured b{font-weight:500}
.featured .dir{display:block;margin-top:9px;font-size:7.5px;font-weight:700;color:var(--blue)}
.view-all{position:absolute;left:13px;top:157px;width:82px;height:26px;border-radius:3px;background:linear-gradient(#333,#1b1b1b);color:#fff;font-size:9px;font-weight:500;text-align:center;line-height:26px}
.f-grey{background:linear-gradient(#a9a9a9,#dedede 45%,#ececec);border:1px solid #c9c9c9}
.f-gold{background:linear-gradient(var(--gold-top),var(--gold-bot));border:1px solid #a8823a}
.f-light{background:linear-gradient(#b8b8b8,#ececec 45%,#f8f8f8);border:1px solid #d0d0d0}
.f-amber{background:linear-gradient(var(--amber-top),var(--amber-bot));border:1px solid #b27222}

/* listings */
.listing{position:absolute;width:248px;border:1px solid var(--line);border-radius:2px;background:#fff;padding:12px 12px 0;font-size:9.5px;line-height:15px;box-shadow:0 8px 7px -7px rgba(0,0,0,.2)}
.listing h3{font-size:11px;font-weight:500;color:var(--dark);padding-bottom:9px;border-bottom:1px solid #cfcfcf;margin-bottom:10px;line-height:14px}
.listing .tel{color:var(--orange)}
.listing .dir{display:block;margin-top:9px;font-size:7.5px;font-weight:700;color:var(--blue);padding-bottom:15px}

/* testimonial */
.testimonial{position:absolute;left:56px;top:978px;width:789px;height:100px;border:1px solid #ddd;border-radius:2px;background:#f5f5f5;padding:15px 12px}
.testimonial h2{font-size:12px;font-weight:700;color:var(--blue);margin-bottom:8px}
.testimonial p{font-size:8.4px;line-height:14px;font-style:italic;color:#666}
.testimonial cite{display:block;margin-top:4px;font-size:9.5px;color:var(--orange)}
.arrows{position:absolute;right:14px;top:16px;display:flex;gap:6px}

/* footer */
.site-footer{position:absolute;left:0;top:1104px;width:900px;height:96px;background:var(--footer);color:#ddd;font-size:8px}
.site-footer .brand{left:56px;top:20px;color:#fff;font-size:13px}
.site-footer .brand-dot{background:#fff;width:11px;height:11px}
.copyright{position:absolute;left:56px;top:64px;color:#999}
.copyright b{color:#eee;font-weight:400}
.f-col{position:absolute;top:17px;line-height:14px}
.f-col h4{font-size:8.5px;font-weight:500;color:var(--blue-light);margin-bottom:3px}
.social{display:flex;gap:4px;margin-top:4px}
.social span{width:22px;height:22px;border-radius:2px;background:#5a5a5a}
</style>
</head>
<body>

<header class="site-header">
  <div class="brand"><span class="brand-dot"></span>LocateTaxPros</div>
  <nav class="main-nav"><span>HOME</span><span>ABOUT US</span><span>HOW IT WORKS</span><span>CONTACT US</span></nav>
  <div class="phone-pill">
    <span class="phone-icon"><svg width="14" height="14" viewBox="0 0 24 24"><path fill="#fff" d="M6.6 10.8c1.4 2.8 3.8 5.1 6.6 6.6l2.2-2.2c.3-.3.7-.4 1-.2 1.1.4 2.3.6 3.6.6.6 0 1 .4 1 1V20c0 .6-.4 1-1 1C10.6 21 3 13.4 3 4c0-.6.4-1 1-1h3.5c.6 0 1 .4 1 1 0 1.3.2 2.5.6 3.6.1.3 0 .7-.2 1l-2.3 2.2z"/></svg></span>
    555-204-7810
  </div>
</header>

<div class="hero-band"></div>
<h1 class="page-title">DIRECTORY OF BELLEVUE<br>TAX EXPERTS</h1>

<div class="cta preparer">ARE YOU TAX PREPARER ?<span class="cta-btn">SUBMIT LISTING</span></div>
<div class="cta help">NEED TAX HELP NOW?<span class="cta-btn" style="padding:0 20px">GET STARTED</span></div>

<div class="city-search">
  <label>Select City</label>
  <div class="city-select">Bellevue</div>
  <div class="go-btn">GO</div>
</div>
<div class="rule"></div>

<div class="featured f-grey" style="left:56px">
  <h3>HARBORLINE TAX<br>SERVICE</h3>
  48 Alder Grove Rd, Bellevue<br>WA 98004<br>Phone: <b>(555) 210-4400</b>
  <span class="dir">GET DIRECTION ››</span>
  <span class="view-all">VIEW ALL</span>
</div>
<div class="featured f-gold" style="left:258px">
  <h3>HARBORLINE TAX<br>SERVICE</h3>
  48 Alder Grove Rd, Bellevue<br>WA 98004<br>Phone: <b>(555) 210-4400</b>
  <span class="dir">GET DIRECTION ››</span>
  <span class="view-all">VIEW ALL</span>
</div>
<div class="featured f-light" style="left:461px">
  <h3>HARBORLINE TAX<br>SERVICE</h3>
  48 Alder Grove Rd, Bellevue<br>WA 98004<br>Phone: <b>(555) 210-4400</b>
  <span class="dir">GET DIRECTION ››</span>
  <span class="view-all">VIEW ALL</span>
</div>
<div class="featured f-amber" style="left:664px">
  <h3>HARBORLINE TAX<br>SERVICE</h3>
  48 Alder Grove Rd, Bellevue<br>WA 98004<br>Phone: <b>(555) 210-4400</b>
  <span class="dir">GET DIRECTION ››</span>
  <span class="view-all">VIEW ALL</span>
</div>

<!-- row 1 -->
<div class="listing" style="left:56px;top:529px"><h3>MARLOW, PETER, CPA</h3>320 W Lindell St<br>Bellevue, WA 98004<br>Phone: <span class="tel">(555) 318-2600</span><span class="dir">GET DIRECTION ››</span></div>
<div class="listing" style="left:326px;top:529px"><h3>HOLLIS BRANT OF BELLEVUE</h3>320 W Lindell St<br>Bellevue, WA 98004<br>Phone: <span class="tel">(555) 318-2600</span><span class="dir">GET DIRECTION ››</span></div>
<div class="listing" style="left:596px;top:529px"><h3>MARLOW, PETER, CPA</h3>320 W Lindell St<br>Bellevue, WA 98004<br>Phone: <span class="tel">(555) 318-2600</span><span class="dir">GET DIRECTION ››</span></div>
<!-- row 2 -->
<div class="listing" style="left:56px;top:672px"><h3>BOOKKEEPING SERVICE</h3>320 W Lindell St<br>Bellevue, WA 98004<br>Phone: <span class="tel">(555) 318-2600</span><span class="dir">GET DIRECTION ››</span></div>
<div class="listing" style="left:326px;top:672px"><h3>DUNMORE ALICE CPA PC</h3>320 W Lindell St<br>Bellevue, WA 98004<br>Phone: <span class="tel">(555) 318-2600</span><span class="dir">GET DIRECTION ››</span></div>
<div class="listing" style="left:596px;top:672px"><h3>BOOKKEEPING SERVICE</h3>320 W Lindell St<br>Bellevue, WA 98004<br>Phone: <span class="tel">(555) 318-2600</span><span class="dir">GET DIRECTION ››</span></div>
<!-- row 3 -->
<div class="listing" style="left:56px;top:819px"><h3>NORA VANCE AND COMPANY</h3>320 W Lindell St<br>Bellevue, WA 98004<br>Phone: <span class="tel">(555) 318-2600</span><span class="dir">GET DIRECTION ››</span></div>
<div class="listing" style="left:326px;top:819px"><h3>KELL-NORWOOD ACCOUNTING</h3>320 W Lindell St<br>Bellevue, WA 98004<br>Phone: <span class="tel">(555) 318-2600</span><span class="dir">GET DIRECTION ››</span></div>
<div class="listing" style="left:596px;top:819px"><h3>NORA VANCE AND COMPANY</h3>320 W Lindell St<br>Bellevue, WA 98004<br>Phone: <span class="tel">(555) 318-2600</span><span class="dir">GET DIRECTION ››</span></div>

<section class="testimonial">
  <h2>WHAT OUR TAX PREPARER SAYS...</h2>
  <div class="arrows">
    <svg width="8" height="10" viewBox="0 0 8 10"><path d="M6 1L2 5l4 4" fill="none" stroke="#666" stroke-width="1.2"/></svg>
    <svg width="8" height="10" viewBox="0 0 8 10"><path d="M2 1l4 4-4 4" fill="none" stroke="#666" stroke-width="1.2"/></svg>
  </div>
  <p>“ Lorem Ipsum is simply dummy text of the printing and typesetting industry. Lorem Ipsum has been the industry's standard dummy text ever since the 1500s, when an unknown printer Aenean a nibh eget turpis vehicula tempus ac sed massa. Vestibulum dolor nulla, ultrices ac tincidunt sed, laoreet non est. Suspendisse lobortis turpis in odio blandit ac interdum lorem euismod.....”</p>
  <cite>-Name Heading</cite>
</section>

<footer class="site-footer">
  <div class="brand"><span class="brand-dot"></span>LocateTaxPros</div>
  <div class="copyright">Copyright © 2015. <b>LocateTaxPros</b>. All Rights Reserved.</div>
  <div class="f-col" style="left:305px"><h4>NAVIGATION</h4>Directory<br>Special Offers<br>Contact Us</div>
  <div class="f-col" style="left:428px"><h4>CONTACT</h4>PO Box 4410<br>Ashford, CT<br>06090</div>
  <div class="f-col" style="left:550px"><h4>LEGAL</h4>Pixel Harbor © 2015<br>website design<br>by brightfieldstudio.com</div>
  <div class="f-col" style="left:718px"><h4>CONNECT US</h4>
    <div class="social"><span></span><span></span><span></span><span></span><span></span></div>
  </div>
</footer>

</body>
</html>
```